Asian Speciality Coffee label for brown valve bag. YUNNAN.

We are in need of a front and back coffee label for a brown paper valve bag.

Our brand is Lotu Brewa. We source the finest and rarest varieties of coffee from the four corners of South East Asia that have been until now kept secret. Our selection has been cultivated by tribal communities and micro lot farmers who for generations have taken pride in organically producing truly amazing coffees. The result is coffee unlike any we have ever tasted before, truly showing how special Asian kapé can be. We believe every bean is precious which is why we ensure all our coffees are sourced ethically through direct trade, roasted by specialists and treated with utmost respect to fulfill our promise of serving you kapé that gives happiness in every cup.

The design of the label will encompass our Company Name logo and signature drinking buddha logo. We want a logo that stands out but at the sane time clearly displaying the finer details of the coffee, such as taste notes, variety etc.

The particular variety we want a label for is called YUNNAN.
Complete details of the coffee are found on our websitehttp://www.lotubrewa.example/shop/yunnan

The front of the bag I would ideally like a picture of the farmer, of which I have provided on website or attached. Together with the name of the coffee and our company logo. Perhaps further details of the coffee can be found on the back. But would like to see creative input.

please look up our website to read more about us. www.lotubrewa.example

Target Market(s)

Speciality Coffee

Requirements
Must have
• Company name logo Lotu Brewa, Drinking Buddha stamp. Details about the coffee. Product name: Yunnan.
• Product details can be found here http://www.lotubrewa.example/shop/yunnan
• or
• Origin: Yunnan Province, Southern China
• Variety: Arabica - Catimor
• Altitude Grown: 1100 - 1400 ft
• Farmer: Co-operative of micro lots
• Process: Fully Washed
• Yunnan’, in local dialect means ‘South of the Cloud’. The Yunnan province located in Southern China is graced with world renowned scenic beauty for its tranquil mountainous valleys. The name we chose for this coffee originated from the location of the coffee trees growing south of the Yunling Mountains (known to locals as Cloud Mountain).Our ‘Yunnan’ coffee is grown south of the Yunling in the rolling hills of Bao Shan and Kunming at an altitude of 1100 - 1400 meters. Pairing organic farming methods and top grade washing and sorting facilities have allowed the farms we work with to perfect their coffee to specialty grade quality. The result of their hard work and dedication to their harvest was evident to us from our first cup.
Should not have
• sticker label will be on a brown paper bag.

```html
<!DOCTYPE html>
<html lang="en">
<head>
<meta charset="utf-8">
<title>Lotu Brewa – Yunnan Coffee Label</title>
<link rel="stylesheet" href="https://fonts.googleapis.com/css2?family=Bebas+Neue&family=Pacifico&family=Noto+Sans+SC:wght@700&family=Roboto:wght@400&display=swap">
<style>
  :root {
    --gold: #d6a34e;
    --gold-deep: #a97a2f;
    --gold-dark: #5b4420;
    --black: #0a0a0a;
    --white: #ffffff;
    --page: #ffffff;
  }
  * { margin: 0; padding: 0; box-sizing: border-box; }
  html, body { width: 1200px; height: 900px; overflow: hidden; background: var(--page); }
  .stage { position: relative; width: 1200px; height: 900px; }

  .label {
    position: absolute; left: 411px; top: 15px; width: 348px; height: 873px;
    background: var(--gold); overflow: hidden;
  }

  .brand-box {
    position: absolute; left: 110px; top: 0; width: 128px; height: 113px;
    background: var(--black); border: 2px solid var(--black);
    outline: 2px solid var(--gold); outline-offset: -8px;
    display: flex; align-items: center; justify-content: center; text-align: center;
  }
  .brand-name {
    font-family: "Bebas Neue", sans-serif; color: var(--gold);
    font-size: 30px; line-height: 0.95; letter-spacing: 1px;
  }

  .farmer-photo {
    position: absolute; left: 0; top: 165px; width: 348px; height: 420px;
    background: linear-gradient(180deg, var(--gold) 0%, #b98b3e 30%, #7a5a27 65%, #8f6b30 100%);
  }

  .lower-panel { position: absolute; left: 0; top: 0; width: 348px; height: 873px; }

  .buddha-stamp {
    position: absolute; left: 128px; top: 412px; width: 92px; height: 100px;
  }

  .product-badge {
    position: absolute; left: 92px; top: 510px; width: 164px; height: 82px;
    background: var(--gold); border-radius: 12px;
    text-align: center;
  }
  .product-name {
    font-family: "Bebas Neue", sans-serif; color: var(--black);
    font-size: 56px; line-height: 1; margin-top: 8px; letter-spacing: 0.5px;
  }
  .product-name-cn {
    font-family: "Noto Sans SC", sans-serif; font-weight: 700; color: var(--black);
    font-size: 16px; line-height: 1; margin-top: -4px;
    display: flex; align-items: center; justify-content: center; gap: 6px;
  }
  .product-name-cn::before, .product-name-cn::after {
    content: ""; width: 30px; height: 2px; background: var(--black);
  }

  .variety {
    position: absolute; left: 0; width: 348px; top: 636px; text-align: center;
    font-family: "Pacifico", cursive; color: var(--gold); font-size: 30px; line-height: 1.2;
  }
  .origin {
    position: absolute; left: 0; width: 348px; top: 680px; text-align: center;
    font-family: "Pacifico", cursive; color: var(--white); font-size: 15px; line-height: 1.2;
  }

  .taste-notes {
    position: absolute; left: 36px; top: 744px; width: 280px;
    display: flex; justify-content: space-between; list-style: none;
  }
  .taste-note { width: 70px; text-align: center; }
  .taste-note svg { display: block; margin: 0 auto 6px; width: 26px; height: 26px; }
  .taste-note span {
    font-family: "Bebas Neue", sans-serif; color: var(--gold); font-size: 12px; letter-spacing: 0.3px;
  }

  .roast-date {
    position: absolute; left: 22px; top: 841px; width: 222px; height: 32px;
    background: var(--gold); padding: 7px 10px;
    font-family: "Bebas Neue", sans-serif; color: var(--black); font-size: 18px; line-height: 1;
  }
  .net-weight {
    position: absolute; left: 270px; top: 844px;
    font-family: "Roboto", sans-serif; color: var(--white); font-size: 18px;
  }
</style>
</head>
<body>
<div class="stage">
  <section class="label">
    <div class="farmer-photo" role="img" aria-label="Sepia photograph of a farmer raking coffee beans drying in the sun"></div>

    <svg class="lower-panel" viewBox="0 0 348 873" aria-hidden="true">
      <polygon points="0,583 348,494 348,873 0,873" fill="var(--gold)"/>
      <polygon points="0,589 348,500 348,873 0,873" fill="var(--black)"/>
    </svg>

    <div class="brand-box"><span class="brand-name">Lotu<br>Brewa</span></div>

    <svg class="buddha-stamp" viewBox="0 0 92 100" role="img" aria-label="Drinking buddha stamp">
      <ellipse cx="46" cy="50" rx="44" ry="48" fill="var(--gold)"/>
    </svg>

    <div class="product-badge">
      <h1 class="product-name">YUNNAN</h1>
      <p class="product-name-cn">云南</p>
    </div>

    <h2 class="variety">Arabica - Catimor</h2>
    <p class="origin">Bao Shan, Southern China</p>

    <ul class="taste-notes">
      <li class="taste-note">
        <svg viewBox="0 0 26 26"><path d="M13 8c-3-2-9-1-9 6 0 5 4 10 6 10 1.5 0 2-1 3-1s1.5 1 3 1c2 0 6-5 6-10 0-7-6-8-9-6z" fill="var(--gold)"/><path d="M13 8c0-3 1-5 3-6" stroke="var(--gold)" stroke-width="1.6" fill="none"/></svg>
        <span>Red Apple</span>
      </li>
      <li class="taste-note">
        <svg viewBox="0 0 26 26"><circle cx="13" cy="14" r="10" fill="var(--gold)"/><path d="M4 12c4-4 14-4 18 0" stroke="var(--black)" stroke-width="1.6" fill="none"/></svg>
        <span>Hazelnut</span>
      </li>
      <li class="taste-note">
        <svg viewBox="0 0 26 26"><rect x="6" y="2" width="14" height="22" rx="1" fill="var(--gold)" transform="rotate(10 13 13)"/><path d="M8 9h11M8 15h11M13 4v18" stroke="var(--black)" stroke-width="1.2" transform="rotate(10 13 13)"/></svg>
        <span>Chocolate</span>
      </li>
      <li class="taste-note">
        <svg viewBox="0 0 26 26"><path d="M2 18c4-10 14-12 22-12-2 10-10 15-22 12z" fill="var(--gold)"/><path d="M3 18c6-4 12-7 19-10" stroke="var(--black)" stroke-width="1.2" fill="none"/></svg>
        <span>Green Tea</span>
      </li>
    </ul>

    <div class="roast-date">ROAST DATE :</div>
    <p class="net-weight">250 g</p>
  </section>
</div>
</body>
</html>
```